Web interface for PC desktop app

We need an HTML design for our new PC software.

To get an idea of the project scope, please review the interface draft in the attached files. The screenshot shows almost all dialogs of our product.

Our product is software that allows users to replace static Windows wallpaper with live animated scenes. The program interface consists of a gallery where users can select and download animated scenes, as well as an information area with scene details and current desktop settings. The product will be distributed on the Vexlo platform among the gamer community.

For this project, you need to create an engaging and user-friendly interface using HTML and CSS in two color schemes (black and white). Additionally, you will need to create a colorized version of the main program icon in vector format (a draft of the program icon is attached), design all other program icons, including icons for the title bar, and redraw all other images according to your design style.

Project Requirements:
-Develop a comprehensive design for the application, including icons and images, in two color schemes: dark and light.
-Colorize our main program icon according to your design style.
-Create other UI icons in all sizes from 16x16 to 512x512 pixels, ensuring that other images are suitable for up to 4K monitors.
-Ensure all UI controls have styles for standard Windows states: normal, hovered, active, and disabled.

Deliverables:
-Final design in HTML and CSS format.
-Icons in ICO format.
-Images in PNG format.

• all interface elements, including the program title bar, coded in HTML and CSS.

```html
<!DOCTYPE html>
<html lang="en">
<head>
<meta charset="utf-8">
<title>Live desktop station</title>
<link href="https://fonts.googleapis.com/css2?family=Inter:wght@400;500;600;700&display=swap" rel="stylesheet">
<style>
:root{
  --ink:#111;
  --text:#2a2d33;
  --muted:#6b7280;
  --panel:#f4f5f7;
  --line:#c7ceda;
  --tab:#b7c2cf;
  --tab-soft:#cdd5df;
  --pill:#c9d2dd;
  --btn:#d3dbe5;
  --white:#fff;
  --star:#f5b50a;
}
*{box-sizing:border-box;margin:0;padding:0}
html,body{width:922px;height:1200px;overflow:hidden;background:var(--white)}
body{position:relative;font-family:"Inter",sans-serif;color:var(--text)}
.abs{position:absolute}
.app-frame{left:27px;top:71px;width:876px;height:577px;background:var(--white);box-shadow:0 6px 18px rgba(0,0,0,.08)}
.titlebar{left:37px;top:76px;width:857px;height:33px;background:var(--ink);border-radius:10px 10px 4px 4px;color:#fff;display:flex;align-items:center}
.app-mark{width:20px;height:20px;border-radius:4px;background:#8f9cb0;margin-left:14px}
.app-name{font-size:10px;margin-left:10px;font-weight:400}
.win-ctrl{position:absolute;top:9px;width:13px;height:13px;border:1px solid #9aa3af}
.win-ctrl svg{display:block}
.panel{background:var(--panel);border:1px solid var(--line);border-radius:8px}
.tab{display:flex;align-items:center;justify-content:center;border-radius:4px;font-size:11px;color:#111}
.tab.active{background:var(--tab);color:#fff}
.tab.soft{background:var(--tab-soft)}
.scene{border-radius:4px}
.bezel{background:#1a1a1a;border-radius:0 0 5px 5px}
.bezel.light{background:#b9c3d0}
.stand{height:5px;border-radius:3px;background:#1a1a1a}
.stand.light{background:#b9c3d0}
.info{font-size:7px;color:#222}
.icon-btn{width:20px;height:20px;border-radius:5px;background:var(--btn);display:flex;align-items:center;justify-content:center}
.divider{height:1px;background:#e1e5eb}
.pill{background:var(--pill);border-radius:10px;font-size:7px;display:flex;align-items:center;padding-left:10px}
.pill b{font-weight:700;margin-left:2px}
.small-btn{height:20px;border-radius:6px;background:var(--btn);font-size:7px;color:#8a94a3;display:flex;align-items:center;justify-content:center}
.meta{font-size:7px;color:#7a8494;display:flex;align-items:center;gap:3px}
.dark-btn{background:var(--ink);color:#fff;border-radius:5px;font-size:7px;font-weight:600;display:flex;align-items:center;justify-content:center}
.field{height:21px;border:1px solid var(--line);border-radius:3px;background:#fff;font-size:7px;display:flex;align-items:center;justify-content:space-between;padding:0 10px}
.tile{width:184px;height:116px}
.caption{width:184px;text-align:center;font-size:6.5px;color:#222;letter-spacing:.1px}
.dialog{left:212px;top:681px;width:388px;height:407px;background:#fff;box-shadow:0 4px 16px rgba(0,0,0,.08)}
.dlg-head{left:217px;top:685px;width:379px;height:24px;background:var(--tab-soft);border-radius:4px;display:flex;align-items:center;font-size:9px;color:#222}
.group{border:1px solid var(--line);border-radius:12px;left:224px;width:364px}
.legend{background:#fff;border:1px solid var(--line);border-radius:9px;font-size:7.5px;display:flex;align-items:center;justify-content:center;height:17px}
.dtext{font-size:7.5px;color:#222}
.box{width:8px;height:8px;border:1px solid #a7afbb;display:inline-block;vertical-align:middle;margin-right:8px}
.radio{width:9px;height:9px;border:1px solid #a7afbb;border-radius:50%;display:inline-block;vertical-align:middle;margin-right:8px}
</style>
</head>
<body>

<div class="abs app-frame"></div>

<header class="abs titlebar">
  <span class="app-mark"></span>
  <span class="app-name">Live desktop station</span>
  <span class="win-ctrl" style="left:793px"><svg width="11" height="11"><line x1="3" y1="6" x2="8" y2="6" stroke="#ccc"/></svg></span>
  <span class="win-ctrl" style="left:811px"><svg width="11" height="11"><rect x="3" y="3" width="5" height="5" fill="none" stroke="#ccc"/></svg></span>
  <span class="win-ctrl" style="left:830px"><svg width="11" height="11"><path d="M3 3L8 8M8 3L3 8" stroke="#ccc"/></svg></span>
</header>

<!-- Left panel -->
<section class="abs panel" style="left:41px;top:123px;width:241px;height:498px"></section>
<div class="abs tab active" style="left:46px;top:128px;width:110px;height:25px">Wallpapers</div>
<div class="abs tab soft" style="left:165px;top:128px;width:110px;height:25px">Screensavers</div>

<div class="abs scene" role="img" aria-label="Abstract swirling colourful wallpaper preview" style="left:50px;top:160px;width:105px;height:68px;background:linear-gradient(135deg,#d23a9a,#3b5bd6 45%,#2ab3d8 70%,#f07a3a)"></div>
<div class="abs bezel" style="left:50px;top:228px;width:105px;height:16px"></div>
<div class="abs" style="left:101px;top:233px;width:4px;height:4px;background:#000"></div>
<div class="abs stand" style="left:82px;top:250px;width:42px"></div>

<div class="abs scene" role="img" aria-label="Sunset sky with lone figure screensaver preview" style="left:167px;top:160px;width:106px;height:68px;background:linear-gradient(180deg,#2d3a5a,#c3502a 55%,#f29a2e 75%,#3a2a2a)"></div>
<div class="abs bezel light" style="left:167px;top:228px;width:106px;height:16px"></div>
<div class="abs" style="left:218px;top:233px;width:4px;height:4px;background:#e7ebf0"></div>
<div class="abs stand light" style="left:199px;top:250px;width:42px"></div>

<div class="abs info" style="left:51px;top:270px">Display : Norvex N2420HD</div>
<div class="abs info" style="left:51px;top:286px">Background : &lt;System Settings&gt;</div>

<div class="abs icon-btn" style="left:184px;top:277px"><svg width="9" height="9" viewBox="0 0 10 10"><circle cx="5" cy="5" r="3" fill="none" stroke="#8a94a3" stroke-width="2" stroke-dasharray="1.5 1"/></svg></div>
<div class="abs icon-btn" style="left:207px;top:277px"><svg width="8" height="8"><path d="M2 1L7 4L2 7Z" fill="#8a94a3"/></svg></div>
<div class="abs icon-btn" style="left:230px;top:277px"><svg width="8" height="8"><rect x="2" y="2" width="5" height="5" fill="#8a94a3"/></svg></div>
<div class="abs icon-btn" style="left:253px;top:277px"><svg width="8" height="8"><rect x="2" y="1.5" width="1.5" height="5" fill="#8a94a3"/><rect x="5" y="1.5" width="1.5" height="5" fill="#8a94a3"/></svg></div>

<div class="abs divider" style="left:46px;top:314px;width:231px"></div>

<div class="abs pill" style="left:50px;top:321px;width:102px;height:18px">Name : <b>Shadow Vanguard</b></div>
<div class="abs scene" role="img" aria-label="Hooded hero leaping through a cloudy sky" style="left:50px;top:347px;width:222px;height:126px;background:radial-gradient(circle at 45% 75%,#f3efe8,#9fb0c3 40%,#3d4f66 100%)"></div>

<div class="abs small-btn" style="left:52px;top:480px;width:33px">Apply</div>
<div class="abs small-btn" style="left:89px;top:480px;width:29px">Test</div>
<div class="abs small-btn" style="left:122px;top:480px;width:19px"><svg width="7" height="8"><rect x="1" y="2" width="5" height="6" fill="#8a94a3"/><rect x="0" y="0.5" width="7" height="1" fill="#8a94a3"/></svg></div>

<div class="abs meta" style="left:52px;top:509px">Autor : <span style="width:13px;height:13px;background:#7f8da0;border-radius:3px;display:inline-block"></span> Pixel Grove</div>
<div class="abs meta" style="left:52px;top:529px">Resolution : 3840x2400</div>
<div class="abs meta" style="left:52px;top:543px">Size : #NAN Mb</div>
<div class="abs meta" style="left:52px;top:557px">Rating :
  <svg width="52" height="8" viewBox="0 0 52 8">
    <g fill="var(--star)"><path id="st" d="M4 0L5 3H8L5.5 5L6.5 8L4 6L1.5 8L2.5 5L0 3H3Z"/><use href="#st" x="10"/><use href="#st" x="20"/><use href="#st" x="30"/></g>
    <use href="#st" x="40" fill="#c6ccd5"/>
  </svg>
</div>
<div class="abs" style="left:155px;top:554px;width:14px;height:13px;border-radius:3px;background:#111;display:flex;align-items:center;justify-content:center"><svg width="8" height="8"><path d="M1 4H3V8H1ZM3 4L5 0.5Q6 1 5.5 3H8L7 8H3Z" fill="var(--star)"/></svg></div>
<div class="abs" style="left:173px;top:554px;width:14px;height:13px;border-radius:3px;background:var(--btn);display:flex;align-items:center;justify-content:center"><svg width="8" height="8"><path d="M1 0H3V4H1ZM3 4L5 7.5Q6 7 5.5 5H8L7 0H3Z" fill="#8a94a3"/></svg></div>

<div class="abs dark-btn" style="left:52px;top:573px;width:115px;height:20px">Create your Own Wallpaper</div>

<!-- Right panel -->
<section class="abs panel" style="left:294px;top:134px;width:598px;height:489px;background:#fff"></section>
<div class="abs" style="left:844px;top:114px;width:15px;height:15px;border-radius:4px;background:var(--btn)"></div>
<div class="abs" style="left:864px;top:114px;width:15px;height:15px;border-radius:4px;background:var(--btn);font-size:7px;color:#8a94a3;display:flex;align-items:center;justify-content:center">i</div>

<div class="abs tab active" style="left:315px;top:127px;width:79px;height:30px;color:#111;box-shadow:0 0 0 2px #fff,0 0 0 3px var(--line)">Installed</div>
<div class="abs tab" style="left:405px;top:134px;width:115px;height:25px;background:#fff;border:1px solid var(--line);border-bottom:none">Workshop LWM1</div>

<div class="abs field" style="left:313px;top:168px;width:156px">Search Wallpaper
  <svg width="8" height="8"><circle cx="3.3" cy="3.3" r="2.5" fill="none" stroke="#111" stroke-width="1.1"/><line x1="5" y1="5" x2="7.5" y2="7.5" stroke="#111" stroke-width="1.2"/></svg></div>
<div class="abs field" style="left:473px;top:168px;width:101px"><span></span><svg width="7" height="5"><path d="M1 1L3.5 3.5L6 1" fill="none" stroke="#111"/></svg></div>
<div class="abs field" style="left:579px;top:168px;width:132px">All<svg width="7" height="5"><path d="M1 1L3.5 3.5L6 1" fill="none" stroke="#111"/></svg></div>
<div class="abs field" style="left:716px;top:168px;width:133px">Top Rated<svg width="7" height="5"><path d="M1 1L3.5 3.5L6 1" fill="none" stroke="#111"/></svg></div>

<div class="abs scene tile" role="img" aria-label="Silhouette on a hill under a red sunset" style="left:313px;top:199px;background:linear-gradient(180deg,#2e3b5e,#c2472a 55%,#f0852f 70%,#2a1d1d)"></div>
<div class="abs scene tile" role="img" aria-label="Starry blue night sky" style="left:500px;top:199px;background:radial-gradient(circle at 40% 45%,#4d8bd0,#123a72 50%,#06142c)"></div>
<div class="abs scene tile" role="img" aria-label="Glowing colourful crystals" style="left:687px;top:199px;background:linear-gradient(100deg,#d8821d,#f2b43a 30%,#b23d8c 60%,#5c2a9c)"></div>
<div class="abs caption" style="left:313px;top:320px">DAWN OF THE TOMORROW</div>
<div class="abs caption" style="left:500px;top:320px">NIGHT SKY STARS</div>
<div class="abs caption" style="left:687px;top:320px">COLOURFUL BACKGROUND</div>

<div class="abs scene tile" role="img" aria-label="Golden sunrise over mountain range" style="left:313px;top:336px;background:radial-gradient(circle at 45% 70%,#f7c35a,#a4692a 40%,#2e2214)"></div>
<div class="abs scene tile" role="img" aria-label="Colourful coral reef with fish" style="left:500px;top:336px;background:radial-gradient(circle at 50% 40%,#7fd9e0,#1f8398 45%,#0d2f45)"></div>
<div class="abs scene tile" role="img" aria-label="Fiery sunset over lake and peaks" style="left:687px;top:336px;background:linear-gradient(180deg,#3a2a3a,#e0532a 35%,#f5a13a 60%,#4a2514)"></div>
<div class="abs caption" style="left:313px;top:458px">DAWN OF THE TOMORROW</div>
<div class="abs caption" style="left:500px;top:458px">MARRINE FISH</div>
<div class="abs caption" style="left:687px;top:458px">DAWN OF THE TOMORROW</div>

<div class="abs scene tile" role="img" aria-label="Snowy Christmas trees with lights" style="left:313px;top:474px;background:radial-gradient(circle at 50% 40%,#6d8a7a,#24463a 55%,#0f2219)"></div>
<div class="abs scene tile" role="img" aria-label="Planet edge in starry space" style="left:500px;top:474px;background:radial-gradient(circle at 0% 50%,#b9bcc4,#4a4d5a 35%,#1e1628 60%,#0c0a14)"></div>
<div class="abs scene tile" role="img" aria-label="Iridescent soap bubbles" style="left:687px;top:474px;background:radial-gradient(circle at 50% 50%,#f0a6d8,#8a4fc8 45%,#2a2c6a)"></div>
<div class="abs caption" style="left:313px;top:596px">CHRISTMAS TREE</div>
<div class="abs caption" style="left:500px;top:596px">SPACE</div>
<div class="abs caption" style="left:687px;top:596px">BUBBLES</div>

<!-- Display settings dialog -->
<div class="abs dialog"></div>
<div class="abs dlg-head">
  <svg style="margin:0 10px 0 7px" width="10" height="10" viewBox="0 0 10 10"><circle cx="5" cy="5" r="3.2" fill="none" stroke="#111" stroke-width="2.2" stroke-dasharray="1.6 1"/><circle cx="5" cy="5" r="1" fill="#111"/></svg>
  Display Settings
  <svg style="margin-left:auto;margin-right:12px" width="7" height="7"><path d="M1 1L6 6M6 1L1 6" stroke="#111" stroke-width="1.2"/></svg>
</div>
<div class="abs dtext" style="left:228px;top:720px;font-size:8.5px">Monitor 1</div>
<div class="abs" style="left:226px;top:733px;width:41px;height:1.5px;background:var(--tab)"></div>
<div class="abs dtext" style="left:279px;top:720px;font-size:8.5px">Monitor 2</div>

<div class="abs group" style="top:747px;height:82px"></div>
<div class="abs legend" style="left:242px;top:740px;width:71px">Video Adapter</div>
<div class="abs dtext" style="left:245px;top:772px">Name : Corelink HD Graphics 620</div>
<div class="abs dtext" style="left:245px;top:783px">Rendering : HAL</div>
<div class="abs dtext" style="left:245px;top:800px"><span class="box"></span>Disable hardware 3D rendering</div>

<div class="abs group" style="top:843px;height:63px"></div>
<div class="abs legend" style="left:242px;top:837px;width:71px">Monitor Usage</div>
<div class="abs dtext" style="left:244px;top:867px"><span class="radio"></span>Display Screen Saver on this monitor</div>
<div class="abs dtext" style="left:244px;top:883px"><span class="radio"></span>Display nothing on this monitor</div>

<div class="abs group" style="top:921px;height:63px"></div>
<div class="abs legend" style="left:242px;top:914px;width:71px">Display mode</div>
<div class="abs dtext" style="left:244px;top:939px">Display mode for this video adapter :</div>
<div class="abs field" style="left:388px;top:933px;width:117px;height:18px;background:#f3f5f8">Automatic<svg width="7" height="5"><path d="M1 1L3.5 3.5L6 1" fill="none" stroke="#111"/></svg></div>
<div class="abs dtext" style="left:244px;top:954px;width:330px;line-height:11.5px">Note : The Automatic display mode finds a mode that works well with your current screen saver settings and video adapter.</div>

<div class="abs group" style="top:998px;height:36px"></div>
<div class="abs legend" style="left:242px;top:992px;width:96px">Dual Monitor Settings</div>
<div class="abs dtext" style="left:243px;top:1017px"><span class="box"></span>Show images in reverse order</div>

<div class="abs dark-btn" style="left:227px;top:1045px;width:35px;height:20px;border-radius:10px">OK</div>
<div class="abs dark-btn" style="left:265px;top:1045px;width:55px;height:20px;border-radius:10px;background:#e6ebf1;color:#111;border:1px solid var(--line)">Cancel</div>

</body>
</html>
```